Halvern Aid Collective Business Card

I'm in desperate need of some very creative design ideas for a progressive growing long term care business. You can get a pretty good idea of who we are by going to our new website that's about to be launched at halvernaidcollective.net. Halvern Aid Collective merely represents and ties together my two operating companies, Halvern Hearthside and Halvern Elder Residences. I need ideas how to represent this on a small business card and make the name and info legible for a senior patient to read. I'm truly looking forward to seeing what creative ideas come out of this process. I think we will need to have a front and back designed business card to allow for space. I also need to make sure our QR code will fit somewhere as well. I've attached a design of a card that was done, but we're not committed to. Design away!!
I've added the EPS versions of the logos. None of the logos need to include the tagline...."Someone you can depend on", unless you think they should or it should be included in the design elsewhere.
Please ask questions freely. Thank you.
Target Market(s)
Senior market, long term care clients.
Industry/Entity Type
Small Business
Look and feel
Each slider illustrates characteristics of the customer's brand and the style your logo design should communicate.

```html
<!DOCTYPE html>
<html lang="en">
<head>
<meta charset="utf-8">
<title>Halvern Aid Collective Business Card</title>
<link rel="stylesheet" href="https://fonts.googleapis.com/css2?family=Sorts+Mill+Goudy&family=Tinos:wght@400;700&display=swap">
<style>
  :root {
    --bg: #e4e5e5;
    --teal: #7db1a0;
    --teal-dark: #72a694;
    --teal-light: #8dbfae;
    --charcoal: #58585a;
    --ink: #3a3a3a;
    --white: #ffffff;
  }
  * { margin: 0; padding: 0; box-sizing: border-box; }
  html, body { width: 1200px; height: 929px; overflow: hidden; }
  body { background: var(--bg); position: relative; font-family: "Tinos", serif; }

  .card { position: absolute; width: 620px; height: 354px; border-radius: 14px; overflow: hidden; }

  /* Front */
  .card-front { left: 60px; top: 150px; background: var(--white); }
  .front-waves { position: absolute; inset: 0; }
  .front-mark { position: absolute; left: 142px; top: 132px; width: 72px; height: 72px; border-radius: 10px; background: var(--teal); }
  .front-name { position: absolute; left: 88px; top: 218px; font-family: "Sorts Mill Goudy", serif; font-size: 72px; line-height: 1; color: var(--charcoal); }
  .divider { position: absolute; left: 372px; top: 72px; width: 2px; height: 220px; background: var(--teal); }
  .contact { position: absolute; left: 392px; top: 72px; color: var(--ink); font-size: 12px; line-height: 1.3; }
  .person { font-weight: 700; font-size: 16px; color: var(--teal); letter-spacing: 0.5px; }
  .role { font-weight: 700; font-size: 12px; margin-bottom: 46px; }
  .address { margin-bottom: 14px; }
  .line { display: flex; align-items: center; gap: 5px; }
  .line svg { width: 11px; height: 11px; fill: var(--teal); }
  .web { margin-top: 20px; }
  .web span { color: var(--teal); }

  /* Back */
  .card-back { left: 520px; top: 530px; background: var(--teal); }
  .back-panel { position: absolute; left: 0; top: 0; width: 260px; height: 290px; background: var(--teal-light); border-bottom-right-radius: 34px; }
  .back-name { position: absolute; right: 26px; bottom: 28px; font-family: "Sorts Mill Goudy", serif; font-size: 68px; line-height: 1; color: var(--white); }

  /* Standalone logo */
  .brand-lockup { position: absolute; left: 850px; top: 120px; width: 250px; text-align: center; }
  .lockup-mark { width: 82px; height: 82px; margin: 0 auto 8px; border-radius: 12px; background: var(--teal); }
  .lockup-name { font-family: "Sorts Mill Goudy", serif; font-size: 70px; line-height: 1; color: var(--charcoal); }
</style>
</head>
<body>

  <section class="card card-front" aria-label="Business card front">
    <svg class="front-waves" viewBox="0 0 620 354" preserveAspectRatio="none" aria-hidden="true">
      <path d="M0 0 H620 V0 C560 10 500 40 430 60 C320 90 210 80 120 120 C70 140 30 170 0 200 Z" fill="var(--teal)"/>
      <path d="M0 0 H620 C560 0 500 20 430 38 C320 66 200 62 110 100 C60 120 25 145 0 170 Z" fill="var(--charcoal)"/>
    </svg>
    <div class="front-mark" aria-hidden="true"></div>
    <div class="front-name">Halvern</div>
    <div class="divider" aria-hidden="true"></div>
    <div class="contact">
      <div class="person">MARTIN ECKER</div>
      <div class="role">Owner</div>
      <div class="address">142 Larkfield Rd.<br>Brennick, Ontario<br>K7R 2M4</div>
      <div class="line">
        <svg viewBox="0 0 24 24" aria-hidden="true"><path d="M6.6 10.8a15 15 0 0 0 6.6 6.6l2.2-2.2a1 1 0 0 1 1-.25 11 11 0 0 0 3.6.6 1 1 0 0 1 1 1V20a1 1 0 0 1-1 1A17 17 0 0 1 3 4a1 1 0 0 1 1-1h3.5a1 1 0 0 1 1 1 11 11 0 0 0 .6 3.6 1 1 0 0 1-.25 1z"/></svg>
        613-555-0148
      </div>
      <div class="line">
        <svg viewBox="0 0 24 24" aria-hidden="true"><path d="M2 5h20v14H2z M2 5l10 8 10-8" stroke="var(--white)" stroke-width="1.5"/></svg>
        martin@halverngroup.ca
      </div>
      <div class="web">www.<span>halvernaidcollective</span>.net</div>
    </div>
  </section>

  <section class="card card-back" aria-label="Business card back">
    <div class="back-panel" aria-hidden="true"></div>
    <div class="back-name">Halvern</div>
  </section>

  <div class="brand-lockup" aria-label="Halvern brand lockup">
    <div class="lockup-mark" aria-hidden="true"></div>
    <div class="lockup-name">Halvern</div>
  </div>

</body>
</html>
```